Broschüre
Zielgruppe
Wir sind ein Projekt-Zusammenschluss aus zwei Firmen im Bereich Fahrzeugeinrichtungen/ Fahrzeugbau und planen eine gemeinsame Vertriebskampagne. Wir vertreiben und montieren in den eigenen Werkstätten Fahrzeugeinrichtungs-Systeme der Marke Kalvera (Marktführer) für Handwerker, Behörden und Versorger. Die Zielgruppe unserer Vertriebskampagne sind vorrangig Nutzfahrzeugverkäufer und Handwerker.
Die Broschüre sollen jeweils im CD der Firmen Wolter und Hallberg gestaltet werden - nachrangig sollen Partner der Firmen Wolter und Hallberg mit angegeben werden, wie zum Beispiel Autohäuser.
Aufgabenstellung
Wir beabsichtigen eine 8-seitige Broschüre im DIN A4-Format mit folgenden Inhalten:
- Vorstellung des Produktes
- Angebote (standardisierte Fahrzeugeinrichtungssysteme )
- Basic-Variante (eher spartanisch) und Pro-Variante (Allrounder - hohe Funktionalität)
- jeweils für kleine und mittlere Transporter
In Summe werden es ca. 10 Einrichtungssysteme (jeweils 5 Stk. für kleine und 5 Stk. für mittlere Transporter)
Text in ArialNarrow

```html
<!DOCTYPE html>
<html lang="de">
<head>
<meta charset="utf-8">
<title>Produktvorstellung – Wolter &amp; Hallberg</title>
<link rel="stylesheet" href="https://fonts.googleapis.com/css2?family=Roboto+Condensed:wght@400;700&display=swap">
<style>
  :root {
    --blue: #1768ad;
    --text: #1c1c1c;
    --white: #ffffff;
  }
  * { margin: 0; padding: 0; box-sizing: border-box; }
  html, body { width: 848px; height: 1200px; overflow: hidden; background: var(--white); }
  body { font-family: "Roboto Condensed", "Arial Narrow", sans-serif; color: var(--text); }
  .page { position: relative; width: 848px; height: 1200px; overflow: hidden; }

  .header-shapes { position: absolute; left: 0; top: 0; }
  .header-title {
    position: absolute; left: 250px; top: 30px; width: 350px;
    text-align: center; font-size: 36px; line-height: 53px; font-weight: 400; color: #000;
  }
  .brand {
    position: absolute; display: flex; align-items: center; gap: 9px;
    font-weight: 400; white-space: nowrap;
  }
  .brand .mark { width: 14px; height: 14px; border-radius: 50%; flex: none; }
  .brand-left { left: 30px; top: 56px; font-size: 24px; color: var(--white); }
  .brand-left .mark { background: var(--white); }
  .brand-right { left: 655px; top: 62px; font-size: 26px; color: var(--text); }
  .brand-right .mark { background: var(--text); }

  .intro {
    position: absolute; left: 26px; top: 172px; width: 796px;
    font-size: 16px; line-height: 23.5px; text-align: justify;
  }
  .features { position: absolute; left: 129px; top: 322px; list-style: none; }
  .features li {
    display: flex; align-items: center; gap: 7px;
    height: 28px; font-size: 16px;
  }
  .features svg { width: 16px; height: 16px; flex: none; }

  .photo { position: absolute; width: 279px; height: 258px; }
  .photo-one { left: 53px; top: 495px; background: linear-gradient(160deg, #cfd4da 0%, #7c8591 45%, #3b4250 70%, #d8dbe0 100%); }
  .photo-two { left: 519px; top: 830px; background: linear-gradient(170deg, #e9ecef 0%, #5b6470 40%, #2f3540 65%, #8a96a6 100%); }

  .product h2 {
    position: absolute; font-weight: 400; font-size: 24px; line-height: 28px; color: var(--blue);
  }
  .product p {
    position: absolute; width: 451px;
    font-size: 16px; line-height: 23.5px; text-align: justify;
  }
  .product-one h2 { left: 343px; top: 494px; }
  .product-one p { left: 343px; top: 524px; }
  .product-two h2 { left: 51px; width: 451px; text-align: right; top: 822px; }
  .product-two p { left: 51px; top: 853px; }

  .divider { position: absolute; left: 190px; top: 794px; width: 474px; height: 1px; background: var(--blue); }

  .footer-shape { position: absolute; left: 0; top: 1114px; }
  .footer-info {
    position: absolute; left: 20px; top: 1130px; width: 200px;
    text-align: center; color: var(--white); font-size: 18px; line-height: 28px;
  }
  .footer-coop {
    position: absolute; left: 290px; top: 1144px; width: 200px;
    text-align: center; color: var(--white); font-size: 18px;
  }
  .footer-left { left: 545px; top: 1145px; font-size: 17px; color: var(--white); }
  .footer-left .mark { width: 10px; height: 10px; background: var(--white); }
  .footer-right { left: 730px; top: 1145px; font-size: 18px; color: var(--text); }
  .footer-right .mark { width: 10px; height: 10px; background: var(--text); }
</style>
</head>
<body>
<div class="page">

  <svg class="header-shapes" width="848" height="146" viewBox="0 0 848 146">
    <polygon points="0,0 310,0 216,143 0,143" fill="var(--blue)"/>
    <polygon points="310,2 528,2 621,142 222,142" fill="var(--white)" stroke="var(--blue)" stroke-width="3"/>
    <line x1="621" y1="142" x2="848" y2="142" stroke="var(--blue)" stroke-width="3"/>
  </svg>
  <div class="brand brand-left"><span class="mark"></span>Wolter Fahrzeugbau</div>
  <h1 class="header-title">Überschrift / Logo<br>Produktvorstellung</h1>
  <div class="brand brand-right"><span class="mark"></span>Hallberg</div>

  <p class="intro">Einleitung: Hallo. Ich bin ein kleiner Blindtext. Und zwar schon so lange ich denken kann. Es war nicht leicht zu verstehen, was es bedeutet, ein blinder Text zu sein: Man ergibt keinen Sinn. Wirklich keinen Sinn. Man wird zusammenhangslos eingeschoben und rumgedreht – und oftmals gar nicht erst gelesen. Aber bin ich allein deshalb ein schlechterer Text als andere? Na gut, ich werde nie in den Bestsellerlisten stehen. Aber andere Texte schaffen das auch nicht. Und darum stört es mich nicht besonders blind zu sein. Und sollten Sie diese Zeilen noch immer lesen, so habe ich als kleiner Blindtext etwas geschafft, wovon all die richtigen und wichtigen Texte meist nur träumen.</p>

  <ul class="features">
    <li><svg viewBox="0 0 16 16"><circle cx="8" cy="8" r="5.2" fill="none" stroke="var(--blue)" stroke-width="4" stroke-dasharray="2.3 1.8"/><circle cx="8" cy="8" r="4.6" fill="var(--blue)"/><circle cx="8" cy="8" r="2" fill="var(--white)"/></svg>Lorem ipsum dolor sit amet, consectetuer adipiscing elit.</li>
    <li><svg viewBox="0 0 16 16"><circle cx="8" cy="8" r="5.2" fill="none" stroke="var(--blue)" stroke-width="4" stroke-dasharray="2.3 1.8"/><circle cx="8" cy="8" r="4.6" fill="var(--blue)"/><circle cx="8" cy="8" r="2" fill="var(--white)"/></svg>Aenean commodo ligula eget dolor.</li>
    <li><svg viewBox="0 0 16 16"><circle cx="8" cy="8" r="5.2" fill="none" stroke="var(--blue)" stroke-width="4" stroke-dasharray="2.3 1.8"/><circle cx="8" cy="8" r="4.6" fill="var(--blue)"/><circle cx="8" cy="8" r="2" fill="var(--white)"/></svg>Aenean massa.</li>
    <li><svg viewBox="0 0 16 16"><circle cx="8" cy="8" r="5.2" fill="none" stroke="var(--blue)" stroke-width="4" stroke-dasharray="2.3 1.8"/><circle cx="8" cy="8" r="4.6" fill="var(--blue)"/><circle cx="8" cy="8" r="2" fill="var(--white)"/></svg>Cum sociis natoque penatibus et magnis dis parturient montes, nascetur ridiculus mus.</li>
    <li><svg viewBox="0 0 16 16"><circle cx="8" cy="8" r="5.2" fill="none" stroke="var(--blue)" stroke-width="4" stroke-dasharray="2.3 1.8"/><circle cx="8" cy="8" r="4.6" fill="var(--blue)"/><circle cx="8" cy="8" r="2" fill="var(--white)"/></svg>Donec quam felis, ultricies nec, pellentesque eu, pretium quis, sem.</li>
  </ul>

  <section class="product product-one">
    <div class="photo photo-one" role="img" aria-label="Foto: Laderaum eines Transporters mit Regal- und Schubladeneinrichtung"></div>
    <h2>Produkt 1</h2>
    <p>Hallo. Ich bin ein kleiner Blindtext. Und zwar schon so lange ich denken kann. Es war nicht leicht zu verstehen, was es bedeutet, ein blinder Text zu sein: Man ergibt keinen Sinn. Wirklich keinen Sinn. Man wird zusammenhangslos eingeschoben und rumgedreht – und oftmals gar nicht erst gelesen. Aber bin ich allein deshalb ein schlechterer Text als andere? Na gut, ich werde nie in den Bestsellerlisten stehen. Aber andere Texte schaffen das auch nicht. Und darum stört es mich nicht besonders blind zu sein. Und sollten Sie diese Zeilen noch immer lesen, so habe ich als kleiner Blindtext etwas geschafft, wovon all die richtigen und wichtigen Texte meist nur träumen.</p>
  </section>

  <div class="divider"></div>

  <section class="product product-two">
    <h2>Produkt 2</h2>
    <p>Hallo. Ich bin ein kleiner Blindtext. Und zwar schon so lange ich denken kann. Es war nicht leicht zu verstehen, was es bedeutet, ein blinder Text zu sein: Man ergibt keinen Sinn. Wirklich keinen Sinn. Man wird zusammenhangslos eingeschoben und rumgedreht – und oftmals gar nicht erst gelesen. Aber bin ich allein deshalb ein schlechterer Text als andere? Na gut, ich werde nie in den Bestsellerlisten stehen. Aber andere Texte schaffen das auch nicht. Und darum stört es mich nicht besonders blind zu sein. Und sollten Sie diese Zeilen noch immer lesen, so habe ich als kleiner Blindtext etwas geschafft, wovon all die richtigen und wichtigen Texte meist nur träumen.</p>
    <div class="photo photo-two" role="img" aria-label="Foto: Transporter mit geöffneter Hecktür und eingebauter Werkstatteinrichtung"></div>
  </section>

  <svg class="footer-shape" width="848" height="86" viewBox="0 0 848 86">
    <polygon points="0,0 738,0 684,86 0,86" fill="var(--blue)"/>
  </svg>
  <p class="footer-info">Informationen, Fußzeile,<br>Adressen</p>
  <p class="footer-coop">In Zusammenarbeit mit</p>
  <div class="brand footer-left"><span class="mark"></span>Wolter Fahrzeugbau</div>
  <div class="brand footer-right"><span class="mark"></span>Hallberg</div>

</div>
</body>
</html>
```